Brochure to advertise our unique physiotherapy clinic to general practitioners

We want to advertise our unique physiotherapy clinic to general practitioners (GPs) to develop there awareness of both our existence and services offered. The brochure should highlight our uniqueness (i.e. providing the highest quality care, advice and education) based on our expert research-based knowledge and skills. After reading the brochure, we want GPs to feel like they know us a little and feel happy to refer their patients to our clinic.
Attached is a draft flyer containing our logo, contact details, profile pictures and the information we would like to be contained in the brochure. We would like the brochure to be A4 double sided and able to be folded to fit into an envelope. More material (pictures) and understanding of our clinic can be found at www.kinetreva.com.au

A brief background of our team:
Our team currently consists of two physiotherapists specialising in the management of musculoskeletal and sports injuries, Dr Howard Tenniscombe and Dr Lionel Fairweather. Both Howard and Lionel have completed PhDs related to musculosketal injury management, and continue to be actively involved in international research groups. Between them they have authored more than 50 peer reviewed papers, presented at countless national and international conferences, and coordinate numerous courses to facilitate professional development of other clinicians. Most importantly, they continue to enjoy mixing these research and teaching activities with treating patients.

Updates
Project Deadline Extended
Reason: Consultation with clinic partner is needed and to allow time for modifications and additional designs. We will pick one, just want quality.
Thanks

Project Deadline Extended

Thank you for some great designs thus far everyone. We have decided to remove the fees from the brochure so please do the same for any future submissions. In the process of trying to provide feedback now.
Thanks
Project Deadline Extended
Reason: A couple of designs are close and we want to allow time to make appropriate modifications. This will be the last extension. Thanks for everyones effort so far

Project Deadline Extended

Target Market(s)
Australian General Practitioners and other health professionals are the targeted audience
Industry/Entity Type
Clinic
Look and feel

```html
<!DOCTYPE html>
<html lang="en">
<head>
<meta charset="utf-8">
<title>Kinetreva Physiotherapy – GP Brochure</title>
<link href="https://fonts.googleapis.com/css2?family=Arimo:ital,wght@0,400;0,700;1,400&display=swap" rel="stylesheet">
<style>
:root{
  --page:#f1f2f4;
  --paper:#ffffff;
  --brand-blue:#1c63ad;
  --band-blue:#1b92d6;
  --brand-green:#8cc63f;
  --soft-green:#e2f1cf;
  --soft-blue:#d3e6f8;
  --ink:#2b2b2b;
  --muted:#666;
  --photo-room:#c9b8a4;
  --photo-treat:#8e9aa6;
  --photo-knee:#6f7781;
  --portrait:#9c8f86;
}
*{box-sizing:border-box;margin:0;padding:0}
html,body{width:1200px;height:927px;overflow:hidden}
body{background:var(--page);font-family:"Arimo",Arial,sans-serif;color:var(--ink);position:relative}
.spread{position:absolute;left:30px;width:1140px;background:var(--paper);display:flex;box-shadow:0 2px 8px rgba(0,0,0,.15)}
.spread--outer{top:16px;height:430px}
.spread--inner{top:464px;height:446px}
.panel{position:relative;height:100%;overflow:hidden;border-right:1px dashed #ddd}
.panel:last-child{border-right:none}

/* wordmark */
.wordmark{display:flex;align-items:center;gap:10px}
.wordmark__dot{width:26px;height:26px;border-radius:50%;background:var(--brand-green)}
.wordmark__name{font-size:34px;font-weight:700;color:var(--brand-blue);letter-spacing:-.5px}
.tagline{font-size:11px;font-style:italic;color:var(--muted);margin-top:2px}

/* intro panel */
.panel--intro{width:300px;padding:24px 0 0}
.panel--intro .wordmark,.panel--intro .tagline{padding-left:22px}
.intro{font-size:8px;line-height:1.45;padding:12px 22px 12px}
.intro::first-letter{font-size:16px;font-style:italic;color:var(--brand-blue)}
.band{background:var(--band-blue);color:#fff;font-weight:700;font-size:13px;padding:5px 22px}
.conditions{list-style:none;columns:2;column-gap:10px;font-size:8px;line-height:1.4;padding:8px 16px 10px 32px}
.conditions li{break-inside:avoid}
.conditions li::before{content:"•";margin-left:-9px;margin-right:5px;color:var(--brand-blue)}
.claims{padding:10px 22px 2px;display:flex;align-items:center;gap:8px}
.claims__sq{width:14px;height:14px;background:var(--brand-blue)}
.claims__name{font-weight:700;font-size:15px;color:var(--brand-blue)}
.claims__note{font-size:9px;font-style:italic;color:var(--muted);padding:0 22px}

/* photo panels */
.panel--photos{width:840px;display:grid;grid-template-columns:300px 1fr;grid-template-rows:150px 1fr;gap:4px;padding:4px;border-right:none}
.photo{display:block;width:100%;height:100%}
.photo--room{grid-column:2;grid-row:1;background:linear-gradient(135deg,#e6ded3,var(--photo-room))}
.photo--knee{grid-column:1;grid-row:1 / span 2;background:linear-gradient(160deg,#b9c0c8,var(--photo-knee))}
.photo--treat{grid-column:2;grid-row:2;background:linear-gradient(150deg,#c7cdd3,var(--photo-treat))}

/* inner spread */
.panel--cover{width:260px;display:flex;flex-direction:column;justify-content:center;padding:0 26px}
.panel--contact{width:140px;display:flex;align-items:flex-end;justify-content:center;padding:24px 0}
.contact{writing-mode:vertical-rl;transform:rotate(180deg);font-size:8px;line-height:1.6;white-space:nowrap;color:var(--muted);font-style:italic}
.panel--content{width:740px;background:linear-gradient(90deg,var(--soft-green) 0%,#ffffff 45%,#ffffff 70%,var(--soft-blue) 100%);padding:16px 0 0}
.section{margin-bottom:8px}
.section .band{display:inline-block;min-width:160px;padding:5px 18px}
.section p{font-size:8.5px;line-height:1.5;padding:6px 24px 0}
.section p::first-letter{font-size:15px;font-style:italic;color:var(--brand-blue)}
.section a{display:block;font-size:8px;color:var(--muted);padding:3px 24px 0;text-decoration:none}
.portraits{display:flex;gap:14px;justify-content:flex-end;padding:0 40px 4px;margin:0}
.portrait{text-align:center;font-size:8px}
.portrait__photo{display:block;width:140px;height:100px;background:linear-gradient(160deg,#c2b8b0,var(--portrait));margin-bottom:3px}
</style>
</head>
<body>

<section class="spread spread--outer">
  <div class="panel panel--intro">
    <div class="wordmark"><span class="wordmark__dot"></span><span class="wordmark__name">Kinetreva</span></div>
    <p class="tagline">Injury experts. Trusted by champions</p>
    <p class="intro">We have the facilities, knowledge and skills to complete comprehensive biomechanical assessments, evidence based exercise prescription, access to a full gym, highly effective manual therapy techniques, injury diagnostic ultrasound, shockwave therapy and foot orthoses. Put together, this will ensure all patients who visit our clinic are given an optimal recovery from almost any musculoskeletal injury, whether acute or chronic.</p>
    <h2 class="band">We treat injuries others cannot fix:</h2>
    <ul class="conditions">
      <li>Achilles tendinopathy</li><li>Patellar tendinopathy</li><li>Tennis elbow</li>
      <li>Rotator cuff injury</li><li>Hamstring tendinopathy</li><li>Gluteal tendon injury</li>
      <li>Plantar fasciitis</li><li>Patellofemoral pain</li><li>Anterior knee pain</li>
      <li>Back and neck pain</li><li>Chronic ankle sprains</li><li>Shoulder pain</li>
      <li>Groin pain</li><li>Hip impingement</li><li>Stress fractures</li>
      <li>Shin splints</li>
    </ul>
    <div class="claims"><span class="claims__sq"></span><span class="claims__name">ClaimPoint</span></div>
    <p class="claims__note">Fast claims... on the spot</p>
  </div>
  <div class="panel panel--photos">
    <span class="photo photo--knee" role="img" aria-label="Physiotherapist assessing a patient's knee on a treatment table"></span>
    <span class="photo photo--room" role="img" aria-label="Clinician treating a patient in a bright clinic room"></span>
    <span class="photo photo--treat" role="img" aria-label="Physiotherapist performing a diagnostic ultrasound on a patient's leg"></span>
  </div>
</section>

<section class="spread spread--inner">
  <div class="panel panel--cover">
    <div class="wordmark"><span class="wordmark__dot"></span><span class="wordmark__name">Kinetreva</span></div>
    <p class="tagline">Injury experts. Trusted by champions</p>
  </div>
  <div class="panel panel--contact">
    <address class="contact">
      Kinetreva Physio, Level 1, 12 Orchard St<br>
      Ashvale East, VIC, 3999<br>
      e: info@kinetreva.com.au<br>
      w: www.kinetreva.com.au<br>
      p: 03 5550 1234
    </address>
  </div>
  <div class="panel panel--content">
    <div class="section">
      <h2 class="band">The Clinic</h2>
      <p>We are a very unique and progressive physiotherapy clinic at Kinetreva, Level 1, 12 Orchard Street, Ashvale East, VIC, 3999. Further information about us is detailed below. Please also check out our website and our 'patellofemoral' and 'biomechanics' blogs if you are interested at:</p>
      <a href="http://www.kinetreva.com.au/">http://www.kinetreva.com.au/</a>
    </div>
    <div class="section">
      <h2 class="band">Who are we?</h2>
      <p>Our team currently consists of two physiotherapists specialising in the management of musculoskeletal and sports injuries, Dr Howard Tenniscombe and Dr Lionel Fairweather. Both Howard and Lionel have completed PhDs related to musculoskeletal injury management, and continue to be actively involved in international research groups. Between them they have authored more than 50 peer reviewed papers, presented at countless national and international conferences, and coordinate numerous courses to facilitate professional development of other clinicians. Most importantly, they continue to enjoy mixing these research and teaching activities with treating patients.</p>
    </div>
    <div class="portraits">
      <figure class="portrait"><span class="portrait__photo" role="img" aria-label="Portrait of Dr Howard Tenniscombe"></span><figcaption>Dr Howard Tenniscombe</figcaption></figure>
      <figure class="portrait"><span class="portrait__photo" role="img" aria-label="Portrait of Dr Lionel Fairweather"></span><figcaption>Dr Lionel Fairweather</figcaption></figure>
    </div>
    <div class="section">
      <h2 class="band">Services offered</h2>
      <p>All patients receive the highest quality 1-1 physiotherapy treatment as we have time to provide accurate, reliable and lasting solutions to their problems. We can guarantee the quality of our treatment because we are genuine experts in musculoskeletal injuries, with a wealth of clinical and research experience. This ultimately means we can provide more effective care, saving patients time and money.</p>
    </div>
  </div>
</section>

</body>
</html>
```